Tarvolinks needs a website to buy and sell phones and electronics

We need a website to buy and sell smartphones.
https://www.grabtradehub.com/
http://www.lumenfoxtrade.co.uk/
http://tradedesk.brindlequaystore.com/
https://www.k7renewal.co.uk/
https://www.coinshiftory.co.uk/we-buy/

I logged into vuqbuild.com and went to their online store template. I iike their template on the camera shop. I like the big letters but with elegance and formality. See link below:
http://www.vuqbuild.com/website-template/view/html/1625?originUrl=http%3A%2F%2Fwww.vuqbuild.com%2Fwebsite%2Ftemplates%2Fhtml%2Fonline-store%2F2&bookName=&galleryDocIndex=0&category=online-store

We know that these websites are too much work but we only need the landing page, without the that big search box. We want the various orvicells such Orvicells 4, 5, 6 and 7 and Dellaro Nimbus S3, S4, S5 and S6 be listed with corresponding prices in Philippine currency.

We don't have a logo yet.

Notes To Designers: I would like to have a good feel of the site and I hope these sites can give you a feel. - grabtradehub.com - lumenfoxtrade.co.uk Note: Please read the brief for updates. Also: i paid for the coded website so I believe it must be a running website. Thank you.

Target Market(s)

Philippines

Industry/Entity Type

Electronics

Coding

Coded - Design and coding required

Number of Pages Required

5+ page

Requirements
Must have
• Must displays phones of Orvicells and Dellaro (Only the latest models for the last 2-3 years) not old
• Tablixes and Wristor as well
Nice to have
• Logo - we need logo
• I love the simplicity but elegance of https://www.grabtradehub.com/

```html
<!DOCTYPE html>
<html lang="en">
<head>
<meta charset="utf-8">
<title>Tarvolinks – Sell or Shop Phones</title>
<link href="https://fonts.googleapis.com/css2?family=Orbitron:wght@500;700&family=Open+Sans:wght@400;600;700&display=swap" rel="stylesheet">
<style>
:root{
  --navy:#1c2638;
  --navy-deep:#141c2b;
  --cyan:#74f0f3;
  --cyan-soft:#cffbfc;
  --cyan-pale:#e9fefe;
  --grey:#ececec;
  --white:#ffffff;
  --red:#e2282d;
  --ink:#1c2638;
  --muted:#6f7785;
}
*{box-sizing:border-box;margin:0;padding:0}
html,body{width:1200px;height:2720px;overflow:hidden}
body{font-family:"Open Sans",Arial,sans-serif;color:var(--ink);background:var(--white);position:relative}
.display{font-family:"Orbitron","Arial Black",sans-serif;text-transform:uppercase;letter-spacing:1px}
section,header,footer{position:absolute;left:0;width:1200px}
.btn{display:inline-block;font-family:"Open Sans",Arial,sans-serif;font-weight:700;font-size:11px;letter-spacing:1px;text-transform:uppercase;border-radius:20px;padding:9px 22px}
.btn-dark{background:var(--navy);color:var(--white)}
.btn-cyan{background:var(--cyan);color:var(--navy)}
.btn-outline{border:1px solid var(--white);color:var(--white)}

/* header */
.site-header{top:0;height:150px;background:var(--navy);color:var(--white)}
.brand{position:absolute;left:190px;top:22px;display:flex;align-items:center;gap:12px}
.brand-dot{width:46px;height:46px;border-radius:50%;border:3px solid var(--cyan)}
.brand-name{font-family:"Orbitron",sans-serif;font-weight:700;font-size:24px;letter-spacing:2px;color:var(--white)}
.cart-note{position:absolute;left:190px;top:82px;font-size:10px;color:#aeb6c4}
.social{position:absolute;left:700px;top:20px;display:flex;gap:6px}
.social span{width:20px;height:20px;border-radius:3px;background:#33405a}
.account{position:absolute;right:190px;top:22px;display:flex;gap:10px}
.account .btn{padding:6px 20px;font-size:10px}
.main-nav{position:absolute;left:190px;right:190px;top:112px;height:26px;border-top:1px solid #33405a;display:flex;justify-content:space-between;align-items:center}
.main-nav a{font-size:10px;color:#d4dae4;text-decoration:none;font-weight:600;padding:0 8px}
.main-nav a.active{color:var(--cyan)}

/* hero */
.hero{top:150px;height:460px;background:linear-gradient(180deg,var(--cyan-soft),var(--cyan-pale));text-align:center;overflow:hidden}
.hero-img{position:absolute}
.hero-tablet{left:-40px;top:10px;width:230px;height:300px;border-radius:18px;background:linear-gradient(135deg,#f2f2f2,#c9cfd6);transform:rotate(-18deg)}
.hero-watch{right:70px;top:0;width:110px;height:110px;border-radius:22px;background:linear-gradient(135deg,#e94a4e,#b8161c);transform:rotate(25deg)}
.hero-phone{right:-10px;top:170px;width:150px;height:280px;border-radius:26px;background:linear-gradient(135deg,#ee3a3f,#a6131a);transform:rotate(-12deg)}
.hero-title{margin-top:52px;font-size:40px;font-weight:700;line-height:1.18;color:var(--navy)}
.search{margin:26px auto 0;width:380px;height:30px;border-radius:15px;background:var(--white);border:1px solid #b9e6e8;display:flex;align-items:center;padding:0 14px;font-size:11px;color:#9aa3ae;justify-content:space-between}
.steps-title{margin-top:34px;font-size:14px;font-weight:700}
.steps{display:flex;justify-content:center;gap:30px;margin-top:20px}
.step{width:180px;text-align:left;display:flex;gap:8px}
.step-icon{flex:0 0 34px;height:34px;border-radius:50%;background:var(--navy);display:flex;align-items:center;justify-content:center}
.step h4{font-size:11px;font-weight:700;margin-bottom:4px}
.step p{font-size:9.5px;color:var(--muted);line-height:1.4}
.hero .btn{margin-top:50px}

/* top devices */
.devices{top:610px;height:400px;background:var(--grey)}
.section-bar{position:absolute;left:140px;right:140px;top:36px;display:flex;justify-content:center;align-items:center;border-bottom:1px solid #cfcfcf;padding-bottom:10px}
.section-bar h2{font-size:15px;font-weight:700}
.arrows{position:absolute;right:0;top:-4px;display:flex;gap:6px}
.arrows span{width:22px;height:22px;background:var(--navy);border-radius:3px;display:flex;align-items:center;justify-content:center}
.device-row{position:absolute;left:140px;top:82px;display:flex;gap:53px}
.device{width:190px;text-align:center}
.device-card{position:relative;height:210px;background:var(--white);border-radius:4px;display:flex;align-items:center;justify-content:center}
.device-tag{position:absolute;left:10px;top:10px;background:var(--navy);color:var(--white);font-size:9px;font-weight:700;padding:4px 8px;border-radius:2px}
.device-img{width:70px;height:150px;border-radius:12px;background:linear-gradient(160deg,#d7dade,#8d939b)}
.device p{margin-top:12px;font-size:11px;font-weight:600}
.devices .btn{position:absolute;left:50%;transform:translateX(-50%);top:348px}

/* split */
.split{top:1010px;height:330px;display:flex}
.split-half{width:600px;height:330px;padding:40px 60px 0;text-align:center}
.split-sell{background:var(--navy);color:var(--white)}
.split-shop{background:var(--cyan);color:var(--navy)}
.split h3{font-size:15px;font-weight:700;line-height:1.35;margin-bottom:28px}
.split-sell h3 em{font-style:normal;color:var(--cyan)}
.split-grid{display:grid;grid-template-columns:repeat(3,1fr);row-gap:26px}
.perk{display:flex;flex-direction:column;align-items:center;gap:8px;font-size:10px;font-weight:600;line-height:1.35}
.perk svg{width:38px;height:30px}

/* why choose */
.why{top:1340px;height:460px;background:var(--grey)}
.why h2{position:absolute;left:280px;top:120px;font-size:30px;font-weight:700}
.why-list{position:absolute;left:280px;top:178px;list-style:none}
.why-list li{display:flex;align-items:center;gap:12px;width:330px;height:34px;margin-bottom:8px;background:var(--navy);color:var(--white);border-radius:17px;padding:0 14px;font-size:12px;font-weight:700;text-transform:uppercase}
.tick{width:20px;height:20px;border-radius:50%;background:var(--cyan);display:flex;align-items:center;justify-content:center}
.why .btn{position:absolute;left:280px;top:318px}
.why-booth{position:absolute;left:640px;top:30px;width:270px;height:430px;border-radius:24px 24px 0 0;background:linear-gradient(180deg,#ee3439,#c21b21)}

/* features */
.features{top:1800px;height:400px;background:var(--cyan)}
.feature-grid{position:absolute;left:230px;top:60px;display:grid;grid-template-columns:380px 380px;row-gap:80px}
.feature{display:flex;gap:18px}
.feature-icon{flex:0 0 80px;height:64px}
.feature h4{font-size:13px;font-weight:700;line-height:1.35;margin-bottom:8px}
.feature p{font-size:9.5px;line-height:1.4;margin-bottom:10px;max-width:240px}
.feature .btn{padding:6px 14px;font-size:9px}

/* trade-in */
.trade{top:2200px;height:220px;background:var(--navy);color:var(--white);overflow:hidden}
.skyline{position:absolute;left:0;bottom:0;width:1200px;height:90px;background:linear-gradient(180deg,rgba(255,255,255,0),rgba(255,255,255,.06))}
.trade h3{position:absolute;left:280px;top:50px;width:400px;font-size:15px;font-weight:500;line-height:1.45}
.trade .btn{position:absolute;left:280px;top:146px;padding:7px 18px}
.trade-shop{position:absolute;left:670px;top:40px;width:190px;height:150px;border-radius:6px 6px 0 0;background:linear-gradient(180deg,#e52b30 0 28%,#3fc7d9 28% 36%,#f2f2f2 36%)}

/* footer */
.site-footer{top:2420px;height:300px;background:var(--navy-deep);color:#c7cdd8}
.foot-brand{position:absolute;left:250px;top:48px}
.foot-brand .brand-name{font-size:18px}
.foot-brand .brand{position:static}
.foot-brand .brand-dot{width:34px;height:34px}
.foot-brand p{margin-top:12px;font-size:9px;line-height:1.5;width:170px;color:#8e97a6}
.foot-brand .social{position:static;margin-top:12px}
.foot-col{position:absolute;top:50px}
.foot-col h5{font-size:10px;font-weight:700;color:var(--white);text-transform:uppercase;letter-spacing:1px;margin-bottom:12px}
.foot-col ul{list-style:none}
.foot-col li{font-size:9px;line-height:1.9}
.col-info{left:480px}
.col-info ul{columns:2;column-gap:24px}
.col-tags{left:620px;width:130px}
.tags{display:flex;flex-wrap:wrap;gap:4px}
.tags span{font-size:8.5px;border:1px solid #3a465c;padding:3px 6px}
.col-posts{left:780px;width:160px}
.post{display:flex;gap:8px;margin-bottom:12px}
.post i{flex:0 0 30px;height:30px;background:#2b374c}
.post span{font-size:9px;line-height:1.4}
.copyright{position:absolute;left:250px;top:262px;font-size:9px;color:#7d8696}
</style>
</head>
<body>

<header class="site-header">
  <div class="brand"><span class="brand-dot"></span><span class="brand-name">TARVOLINKS</span></div>
  <div class="cart-note">0 item(s) – ₱0.00</div>
  <div class="social" aria-label="Social links"><span></span><span></span><span></span></div>
  <div class="account"><span class="btn btn-outline">Log in</span><span class="btn btn-cyan">Register</span></div>
  <nav class="main-nav">
    <a class="active" href="#">Home</a><a href="#">Sell Phone</a><a href="#">Shop</a><a href="#">About Us</a><a href="#">How It Works</a><a href="#">Reviews</a><a href="#">FAQ</a><a href="#">Contact Us</a>
  </nav>
</header>

<section class="hero">
  <div class="hero-img hero-tablet" role="img" aria-label="Photo of a silver tablet"></div>
  <div class="hero-img hero-watch" role="img" aria-label="Photo of a red smartwatch"></div>
  <div class="hero-img hero-phone" role="img" aria-label="Photo of a red smartphone"></div>
  <h1 class="hero-title display">How much can I sell<br>my phone or tablet for?</h1>
  <div class="search">Search for your device<svg width="12" height="12" viewBox="0 0 12 12"><circle cx="5" cy="5" r="4" fill="none" stroke="#1c2638" stroke-width="1.5"/><line x1="8" y1="8" x2="11" y2="11" stroke="#1c2638" stroke-width="1.5"/></svg></div>
  <h3 class="steps-title display">How does it work</h3>
  <div class="steps">
    <div class="step"><span class="step-icon"><svg width="14" height="20" viewBox="0 0 14 20"><rect x="1" y="1" width="12" height="18" rx="2" fill="none" stroke="#74f0f3" stroke-width="1.6"/></svg></span><div><h4>1. Select your device</h4><p>Find your model and pick its condition.</p></div></div>
    <div class="step"><span class="step-icon"><svg width="20" height="16" viewBox="0 0 20 16"><rect x="1" y="3" width="18" height="12" fill="none" stroke="#74f0f3" stroke-width="1.6"/><line x1="1" y1="7" x2="19" y2="7" stroke="#74f0f3" stroke-width="1.6"/></svg></span><div><h4>2. We'll send a free pack</h4><p>A free postage pack comes to your door.</p></div></div>
    <div class="step"><span class="step-icon"><svg width="20" height="16" viewBox="0 0 20 16"><path d="M1 5h12v8H1zM13 8h4l2 3v2h-6" fill="none" stroke="#74f0f3" stroke-width="1.6"/></svg></span><div><h4>3. Post your device to us</h4><p>Drop it off at any courier near you.</p></div></div>
    <div class="step"><span class="step-icon"><svg width="20" height="14" viewBox="0 0 20 14"><rect x="1" y="1" width="18" height="12" rx="1" fill="none" stroke="#74f0f3" stroke-width="1.6"/><circle cx="10" cy="7" r="2.5" fill="none" stroke="#74f0f3" stroke-width="1.6"/></svg></span><div><h4>4. Receive your payment</h4><p>Get paid the same day we receive it.</p></div></div>
  </div>
  <span class="btn btn-dark">Sell your phone</span>
</section>

<section class="devices">
  <div class="section-bar"><h2 class="display">Our top devices</h2>
    <div class="arrows"><span><svg width="8" height="10" viewBox="0 0 8 10"><path d="M6 1L2 5l4 4" fill="none" stroke="#fff" stroke-width="1.6"/></svg></span><span><svg width="8" height="10" viewBox="0 0 8 10"><path d="M2 1l4 4-4 4" fill="none" stroke="#fff" stroke-width="1.6"/></svg></span></div>
  </div>
  <div class="device-row">
    <div class="device"><div class="device-card"><span class="device-tag">SALE</span><div class="device-img" role="img" aria-label="Photo of a grey Orvicell 6s"></div></div><p>Orvicell 6s 16GB – ₱18,500</p></div>
    <div class="device"><div class="device-card"><span class="device-tag">SALE</span><div class="device-img" role="img" aria-label="Photo of a grey Orvicell 6s"></div></div><p>Orvicell 6s 32GB – ₱21,000</p></div>
    <div class="device"><div class="device-card"><span class="device-tag">SALE</span><div class="device-img" role="img" aria-label="Photo of a grey Orvicell 6s"></div></div><p>Orvicell 6s 64GB – ₱24,500</p></div>
    <div class="device"><div class="device-card"><span class="device-tag">SALE</span><div class="device-img" role="img" aria-label="Photo of a grey Orvicell 6s"></div></div><p>Orvicell 6s 128GB – ₱28,000</p></div>
  </div>
  <span class="btn btn-cyan">View more</span>
</section>

<section class="split">
  <div class="split-half split-sell">
    <h3 class="display">Why wouldn't you <em>sell</em><br>with us?</h3>
    <div class="split-grid">
      <div class="perk"><svg viewBox="0 0 38 30"><rect x="2" y="6" width="34" height="18" rx="2" fill="none" stroke="#74f0f3" stroke-width="2"/><circle cx="19" cy="15" r="4" fill="none" stroke="#74f0f3" stroke-width="2"/></svg>Get ₱500 for your<br>first trade</div>
      <div class="perk"><svg viewBox="0 0 38 30"><rect x="6" y="4" width="26" height="22" rx="2" fill="none" stroke="#74f0f3" stroke-width="2"/><line x1="6" y1="11" x2="32" y2="11" stroke="#74f0f3" stroke-width="2"/></svg>Super fast same<br>day payments</div>
      <div class="perk"><svg viewBox="0 0 38 30"><path d="M4 10h20v12H4zM24 14h6l4 4v4H24" fill="none" stroke="#74f0f3" stroke-width="2"/></svg>Free pickup and<br>postage packs</div>
      <div class="perk"><svg viewBox="0 0 38 30"><rect x="13" y="2" width="12" height="26" rx="2" fill="none" stroke="#74f0f3" stroke-width="2"/></svg>We buy broken<br>phones</div>
      <div class="perk"><svg viewBox="0 0 38 30"><circle cx="19" cy="15" r="11" fill="none" stroke="#74f0f3" stroke-width="2"/><path d="M19 8v7l5 3" fill="none" stroke="#74f0f3" stroke-width="2"/></svg>Price lock for<br>14 days</div>
      <div class="perk"><svg viewBox="0 0 38 30"><path d="M8 16l7 7 15-15" fill="none" stroke="#74f0f3" stroke-width="2.4"/></svg>No hidden<br>fees at all</div>
    </div>
  </div>
  <div class="split-half split-shop">
    <h3 class="display">Why wouldn't you shop<br>with us?</h3>
    <div class="split-grid">
      <div class="perk"><svg viewBox="0 0 38 30"><path d="M19 3l12 5v8c0 6-5 10-12 12C12 26 7 22 7 16V8z" fill="none" stroke="#1c2638" stroke-width="2"/></svg>12 month warranty<br>on all devices</div>
      <div class="perk"><svg viewBox="0 0 38 30"><path d="M4 10h20v12H4zM24 14h6l4 4v4H24" fill="none" stroke="#1c2638" stroke-width="2"/></svg>Free delivery on<br>all orders</div>
      <div class="perk"><svg viewBox="0 0 38 30"><path d="M6 8h26l-3 14H9z" fill="none" stroke="#1c2638" stroke-width="2"/></svg>Easy 30 day<br>returns</div>
      <div class="perk"><svg viewBox="0 0 38 30"><rect x="4" y="7" width="30" height="18" rx="2" fill="none" stroke="#1c2638" stroke-width="2"/><line x1="4" y1="12" x2="34" y2="12" stroke="#1c2638" stroke-width="2"/></svg>Pay with cards<br>or e-wallets</div>
      <div class="perk"><svg viewBox="0 0 38 30"><circle cx="19" cy="15" r="11" fill="none" stroke="#1c2638" stroke-width="2"/><path d="M14 15l4 4 7-8" fill="none" stroke="#1c2638" stroke-width="2"/></svg>Fully tested<br>devices</div>
      <div class="perk"><svg viewBox="0 0 38 30"><path d="M19 4l4 8 9 1-7 6 2 9-8-5-8 5 2-9-7-6 9-1z" fill="none" stroke="#1c2638" stroke-width="2"/></svg>Refurbished quality<br>guarantee</div>
    </div>
  </div>
</section>

<section class="why">
  <h2 class="display">Why choose us?</h2>
  <ul class="why-list">
    <li><span class="tick"><svg width="10" height="8" viewBox="0 0 10 8"><path d="M1 4l3 3 5-6" fill="none" stroke="#1c2638" stroke-width="1.8"/></svg></span>Same day payment</li>
    <li><span class="tick"><svg width="10" height="8" viewBox="0 0 10 8"><path d="M1 4l3 3 5-6" fill="none" stroke="#1c2638" stroke-width="1.8"/></svg></span>We love broken phones</li>
    <li><span class="tick"><svg width="10" height="8" viewBox="0 0 10 8"><path d="M1 4l3 3 5-6" fill="none" stroke="#1c2638" stroke-width="1.8"/></svg></span>5 star rating on Trustvela</li>
  </ul>
  <span class="btn btn-cyan">Get started</span>
  <div class="why-booth" role="img" aria-label="Illustration of a red telephone booth"></div>
</section>

<section class="features">
  <div class="feature-grid">
    <div class="feature"><svg class="feature-icon" viewBox="0 0 80 64"><rect x="8" y="14" width="56" height="34" rx="3" fill="none" stroke="#1c2638" stroke-width="3"/><circle cx="36" cy="31" r="8" fill="none" stroke="#1c2638" stroke-width="3"/></svg><div><h4 class="display">We pay on the same day</h4><p>Your money is sent the same day your device arrives.</p><span class="btn btn-dark">Read more</span></div></div>
    <div class="feature"><svg class="feature-icon" viewBox="0 0 80 64"><path d="M6 18h40v28H6zM46 26h14l10 10v10H46" fill="none" stroke="#1c2638" stroke-width="3"/><circle cx="20" cy="48" r="5" fill="#1c2638"/><circle cx="58" cy="48" r="5" fill="#1c2638"/></svg><div><h4 class="display">It's free to post your device</h4><p>We cover the courier cost from anywhere in the country.</p><span class="btn btn-dark">Read more</span></div></div>
    <div class="feature"><svg class="feature-icon" viewBox="0 0 80 64"><rect x="10" y="10" width="52" height="36" rx="2" fill="none" stroke="#1c2638" stroke-width="3"/><path d="M26 56h20M36 46v10" stroke="#1c2638" stroke-width="3"/></svg><div><h4 class="display">Five star rating on Trustvela</h4><p>Thousands of happy sellers rate our service highly.</p><span class="btn btn-dark">Read more</span></div></div>
    <div class="feature"><svg class="feature-icon" viewBox="0 0 80 64"><rect x="10" y="8" width="42" height="50" rx="2" fill="none" stroke="#1c2638" stroke-width="3"/><path d="M18 22h26M18 32h26M18 42h16" stroke="#1c2638" stroke-width="3"/></svg><div><h4 class="display">Online price guarantee</h4><p>The price you see online is the price we pay you.</p><span class="btn btn-dark">Read more</span></div></div>
  </div>
</section>

<section class="trade">
  <div class="skyline" role="img" aria-label="Faint city skyline backdrop"></div>
  <h3 class="display">Otherwise you can trade in your phone or tablet at any of our 888 sell offices!</h3>
  <span class="btn btn-cyan">Find a store</span>
  <div class="trade-shop" role="img" aria-label="Illustration of a small shop front"></div>
</section>

<footer class="site-footer">
  <div class="foot-brand">
    <div class="brand"><span class="brand-dot"></span><span class="brand-name">TARVOLINKS</span></div>
    <p>Buy and sell phones, tablets and watches across the Philippines.</p>
    <div class="social"><span></span><span></span><span></span><span></span></div>
  </div>
  <div class="foot-col col-info"><h5>Information</h5>
    <ul><li>About Us</li><li>Delivery</li><li>Privacy</li><li>Terms</li><li>Returns</li><li>Sitemap</li><li>Contact</li><li>FAQ</li><li>Reviews</li><li>Blog</li></ul>
  </div>
  <div class="foot-col col-tags"><h5>Product Tags</h5>
    <div class="tags"><span>Orvicells</span><span>Dellaro</span><span>Tablixes</span><span>Wristor</span><span>Used</span><span>New</span><span>Broken</span><span>Sale</span></div>
  </div>
  <div class="foot-col col-posts"><h5>Recent Posts</h5>
    <div class="post"><i></i><span>How to wipe your phone<br>Mar 12, 2017</span></div>
    <div class="post"><i></i><span>Best trade-in prices now<br>Mar 08, 2017</span></div>
    <div class="post"><i></i><span>Caring for your tablet<br>Mar 02, 2017</span></div>
  </div>
  <div class="copyright">© 2017 Tarvolinks. All rights reserved.</div>
</footer>

</body>
</html>
```